Home care support

Design a a great and dynamic website for a healthcare business. Our business will be involved in providing care at home for people with disability and the elderly. Below is a link that I found for a company offering similar services in the US. I am looking for something like this .
I have my files - the latest project in here in through through Pixelmarket
Sample site : https://cedarbrookassistedliving.com/
Target Market(s)
people with disability and elderly seniors who need home care support
Industry/Entity Type
Health
Coding
Coded - Design and coding required
Number of Pages Required
5+ page
Requirements
Must have
- inspirational pictures and designed with the themed logo (files attached)
Nice to have
- This is my sample and should look like this : https://cedarbrookassistedliving.com/

```html
<!DOCTYPE html>
<html lang="en">
<head>
<meta charset="utf-8">
<title>Marlow Home Care – Home Care Support</title>
<link href="https://fonts.googleapis.com/css2?family=Poppins:wght@300;400;500;600&display=swap" rel="stylesheet">
<style>
:root{
  --blue:#0b6ea8;
  --blue-dark:#085c8d;
  --green:#5e9b3d;
  --navy:#1f2a44;
  --text:#4a5160;
  --white:#ffffff;
  --line:#c9ced6;
}
*{box-sizing:border-box;margin:0;padding:0}
html,body{width:1200px;height:3676px;overflow:hidden}
body{font-family:'Poppins',sans-serif;color:var(--text);background:var(--white);position:relative}
.abs{position:absolute}
a{color:inherit;text-decoration:none}
svg{display:block}

/* top bar */
.topbar{left:0;top:0;width:1200px;height:40px;background:var(--blue);color:var(--white);font-size:13px}
.topbar .info{position:absolute;right:173px;top:11px;display:flex;gap:20px;align-items:center}
.topbar .info span{display:flex;align-items:center;gap:6px}

/* header */
.brand{display:flex;align-items:center;gap:10px;font-weight:600;color:var(--blue);font-size:30px;letter-spacing:1px}
.brand .dot{width:44px;height:44px;border-radius:50%;background:var(--green)}
.brand small{display:block;font-size:10px;letter-spacing:5px;font-weight:400}
.header-brand{left:171px;top:70px}
.nav{top:64px;left:594px;font-size:14px;color:var(--navy)}
.nav a{position:absolute;white-space:nowrap}
.nav .active{color:var(--green)}

/* hero */
.hero-title{left:171px;top:190px;font-size:63px;font-weight:300;line-height:64px;color:var(--navy)}
.hero-text{left:173px;top:334px;width:330px;font-size:14.5px;line-height:23px}
.btn{display:inline-flex;align-items:center;justify-content:center;background:var(--green);color:var(--white);border-radius:22px;font-size:14px;font-weight:500}
.hero-btn{left:173px;top:425px;width:188px;height:40px}
.hero-ring{left:549px;top:118px;width:480px;height:480px;border-radius:50%;border:8px solid var(--blue);border-left-color:transparent;border-bottom-color:transparent}
.hero-photo{left:557px;top:126px;width:470px;height:430px;border-radius:50%;background:radial-gradient(circle at 60% 40%,#c7d8e6,#8aa9bd 55%,#4b6c82)}

/* features */
.feature{width:260px}
.feature .hex{width:66px;height:72px}
.feature h3{font-size:18px;font-weight:400;color:var(--navy);margin-top:14px}
.feature p{font-size:13.5px;line-height:22px;margin-top:6px}

/* about */
.about-band{left:0;top:1130px;width:1200px;height:383px;background:var(--blue)}
.about-ring{left:123px;top:1092px;width:462px;height:462px;border-radius:50%;border:1.5px solid var(--green)}
.about-photo{left:141px;top:1110px;width:426px;height:426px;border-radius:50%;background:radial-gradient(circle at 50% 45%,#e8ddd2,#bfb3a6 55%,#7d8f9c)}
.eyebrow{font-size:14px;font-weight:500;letter-spacing:3px;color:var(--green)}
.about-copy{left:616px;top:1176px;width:420px;color:var(--white)}
.about-copy h2{font-size:44px;font-weight:400;line-height:54px;margin-top:2px;white-space:nowrap}
.about-copy p{font-size:13.8px;line-height:25px;margin-top:10px}
.about-copy .btn{width:133px;height:40px;margin-top:24px}

/* services */
.section-title{left:0;width:1200px;text-align:center;font-size:46px;font-weight:500;color:var(--navy)}
.service{width:269px;border-bottom:3px solid var(--blue);padding-bottom:14px}
.service .photo{width:269px;height:176px}
.service h3{font-size:19px;font-weight:500;color:var(--navy);margin-top:14px}
.service p{font-size:14px;line-height:24px;margin-top:4px}
.service .more{display:block;color:var(--green);font-size:14px;margin-top:8px}
.view-all{left:522px;top:2058px;width:154px;height:40px}

/* testimonials */
.testi-band{left:0;top:2158px;width:1200px;height:515px;background:var(--blue)}
.testi-head{left:0;top:2212px;width:1200px;text-align:center;color:var(--white)}
.testi-head h2{font-size:43px;font-weight:400;margin-top:2px}
.testi{width:267px;height:265px;background:var(--white);border-radius:3px;text-align:center;padding-top:18px}
.testi svg{margin:0 auto}
.testi p{font-size:13.5px;line-height:25px;padding:8px 12px 0}
.testi .rule{width:22px;height:2px;background:var(--green);margin:10px auto 0}
.testi .avatar{width:56px;height:56px;border-radius:50%;margin:12px auto 0;background:linear-gradient(#d7dde4,#9fb0c0)}
.testi h4{font-size:14px;font-weight:500;color:var(--navy);margin-top:8px;line-height:20px}

/* contact */
.contact-bg{left:0;top:2673px;width:1200px;height:352px;background:linear-gradient(90deg,#f6f7f8,#eceff2 60%,#f3f4f6)}
.contact-title{left:171px;top:2758px;font-size:46px;font-weight:400;color:var(--navy)}
.contact-text{left:173px;top:2829px;width:420px;font-size:14px;line-height:25px}
.field{left:648px;width:379px;border:1px solid #9aa0a8;background:var(--white);font-size:14px;color:var(--text);padding:10px 9px}
.submit{left:909px;top:2947px;width:117px;height:38px}

/* find us */
.map{left:0;top:3025px;width:1200px;height:326px;background:linear-gradient(135deg,#e7e9e6,#dfe6dc 40%,#e8e9ea)}
.find{left:173px;top:3025px;width:265px;height:326px;background:var(--blue);color:var(--white);padding:44px 20px 0}
.find h2{font-size:28px;font-weight:400;margin-top:2px}
.find .row{display:flex;gap:10px;font-size:13px;line-height:23px;margin-top:14px}
.find .row svg{flex:none;margin-top:5px}
.socials{display:flex;gap:9px;margin-top:18px}
.socials span{width:26px;height:26px;border-radius:50%;border:2px solid var(--white)}

/* footer */
.footer-brand{left:173px;top:3460px}
.copy{left:173px;top:3606px;font-size:11.5px;color:var(--text)}
.copy b{color:var(--blue);font-weight:400}
.fcol h4{font-size:16px;font-weight:500;color:var(--navy)}
.fcol p{font-size:13.5px;line-height:21.5px;margin-top:14px}
.fcol ul{list-style:none;margin-top:12px}
.fcol li{font-size:13.5px;line-height:37.5px;padding-left:14px;position:relative}
.fcol li::before{content:"";position:absolute;left:0;top:14px;border-left:5px solid var(--green);border-top:4px solid transparent;border-bottom:4px solid transparent}
.arrow{top:2441px}
</style>
</head>
<body>

<div class="abs topbar">
  <div class="info">
    <span><svg width="12" height="12" viewBox="0 0 24 24" fill="#fff"><path d="M6.6 10.8a15 15 0 0 0 6.6 6.6l2.2-2.2a1 1 0 0 1 1-.25 11.4 11.4 0 0 0 3.6.6 1 1 0 0 1 1 1V20a1 1 0 0 1-1 1A17 17 0 0 1 3 4a1 1 0 0 1 1-1h3.5a1 1 0 0 1 1 1c0 1.25.2 2.45.6 3.6a1 1 0 0 1-.25 1z"/></svg>01 234 567 890</span>
    <span><svg width="13" height="10" viewBox="0 0 24 18" fill="#fff"><path d="M0 0h24v2L12 10 0 2z M0 4l12 8 12-8v14H0z"/></svg>hello@marlowhomecare.com</span>
  </div>
</div>

<header>
  <div class="abs brand header-brand"><span class="dot"></span><div>MARLOW<small>HOMECARE</small></div></div>
  <nav class="abs nav">
    <a class="active" style="left:0">Home</a>
    <a style="left:85px">About</a>
    <a style="left:170px">Services</a>
    <a style="left:271px">FAQ</a>
    <a style="left:343px">Contact</a>
    <svg style="position:absolute;left:419px;top:4px" width="14" height="14" viewBox="0 0 24 24" fill="none" stroke="#1f2a44" stroke-width="3"><circle cx="10" cy="10" r="7"/><path d="M15 15l7 7"/></svg>
  </nav>
</header>

<section class="hero">
  <h1 class="abs hero-title">Home Care<br>Support</h1>
  <p class="abs hero-text">Praesent eu leo porttitor, porta tels dapibus, sodales diam. Cras sollicitudin quam eget varius blandit.</p>
  <a class="abs btn hero-btn">Make An Appointment</a>
  <div class="abs hero-ring"></div>
  <div class="abs hero-photo" role="img" aria-label="Caregiver and elderly woman in a wheelchair looking out a window"></div>
</section>

<section class="features">
  <svg width="0" height="0" style="position:absolute"><defs><path id="hexagon" d="M33 0 66 18v36L33 72 0 54V18z"/></defs></svg>
  <div class="abs feature" style="left:171px;top:628px"><svg class="hex" viewBox="0 0 66 72"><use href="#hexagon" fill="#0b6ea8"/><circle cx="33" cy="30" r="6" fill="none" stroke="#fff" stroke-width="2"/><path d="M22 50v-6a11 11 0 0 1 22 0v6" fill="none" stroke="#fff" stroke-width="2"/></svg><h3>Professional &amp; Friendly Staff</h3><p>Mauris convallis id urna sit amet facilisis. Duis mollis vehicula neque id molestie</p></div>
  <div class="abs feature" style="left:475px;top:628px"><svg class="hex" viewBox="0 0 66 72"><use href="#hexagon" fill="#0b6ea8"/><text x="33" y="40" fill="#fff" font-size="11" font-family="Poppins,sans-serif" text-anchor="middle">24/7</text></svg><h3>On Call 24/7</h3><p>Mauris convallis id urna sit amet facilisis. Duis mollis vehicula neque id molestie</p></div>
  <div class="abs feature" style="left:779px;top:628px"><svg class="hex" viewBox="0 0 66 72"><use href="#hexagon" fill="#0b6ea8"/><rect x="20" y="24" width="26" height="24" rx="2" fill="none" stroke="#fff" stroke-width="2"/><path d="M20 31h26" stroke="#fff" stroke-width="2"/></svg><h3>Flexible Schedule</h3><p>Mauris convallis id urna sit amet facilisis. Duis mollis vehicula neque id molestie</p></div>
  <div class="abs feature" style="left:171px;top:852px"><svg class="hex" viewBox="0 0 66 72"><use href="#hexagon" fill="#0b6ea8"/><circle cx="33" cy="33" r="11" fill="none" stroke="#fff" stroke-width="2"/><path d="M27 48h12" stroke="#fff" stroke-width="2"/></svg><h3>Peace of Mind</h3><p>Mauris convallis id urna sit amet facilisis. Duis mollis vehicula neque id molestie</p></div>
  <div class="abs feature" style="left:475px;top:852px"><svg class="hex" viewBox="0 0 66 72"><use href="#hexagon" fill="#0b6ea8"/><path d="M33 46 21 34a6 6 0 0 1 12-7 6 6 0 0 1 12 7z" fill="none" stroke="#fff" stroke-width="2"/></svg><h3>We Care</h3><p>Mauris convallis id urna sit amet facilisis. Duis mollis vehicula neque id molestie</p></div>
  <div class="abs feature" style="left:779px;top:852px"><svg class="hex" viewBox="0 0 66 72"><use href="#hexagon" fill="#0b6ea8"/><circle cx="27" cy="24" r="4" fill="none" stroke="#fff" stroke-width="2"/><circle cx="39" cy="24" r="4" fill="none" stroke="#fff" stroke-width="2"/><path d="M27 30v18M39 30v18M44 36v12" stroke="#fff" stroke-width="2"/></svg><h3>Quality Caregivers</h3><p>Mauris convallis id urna sit amet facilisis. Duis mollis vehicula neque id molestie</p></div>
</section>

<section class="about">
  <div class="abs about-band"></div>
  <div class="abs about-ring"></div>
  <div class="abs about-photo" role="img" aria-label="Smiling elderly woman with her carer resting hands on her shoulders"></div>
  <div class="abs about-copy">
    <div class="eyebrow">ABOUT</div>
    <h2>Marlow Home Care</h2>
    <p>Vivamus semper eros enim, sed viverra turpis eleifend vitae. Ut nec dolor faucibus, tristique libero ac, rhoncus est. Sed quam orci, pulvinar id dolor a, conseetur egestas magna. Vestibulum ante ipsum primis in faucibus orci luctus et ultrices posuere cubilia curae; Fusca sem sagittis, lobortis erat auctor, varius erat. Cras imperdiet.</p>
    <a class="btn">Read More</a>
  </div>
</section>

<section class="services">
  <h2 class="abs section-title" style="top:1610px">Our Services</h2>
  <div class="abs service" style="left:171px;top:1685px"><div class="photo" role="img" aria-label="Carer bringing a drink to an elderly man at home" style="background:linear-gradient(135deg,#e9e6e1,#b9a999 60%,#6d5a4b)"></div><h3>Medication Reminders</h3><p>Mauris convallis id urna sit amet facilisis. Duis mollis vehicula neque id molestie</p><a class="more">Read More ▸</a></div>
  <div class="abs service" style="left:467px;top:1685px"><div class="photo" role="img" aria-label="Nurse with elderly woman in a wheelchair in a park" style="background:linear-gradient(180deg,#cfe0b5,#8bb35a 60%,#5d8a32)"></div><h3>Domiciliary Care</h3><p>Mauris convallis id urna sit amet facilisis. Duis mollis vehicula neque id molestie</p><a class="more">Read More ▸</a></div>
  <div class="abs service" style="left:761px;top:1685px"><div class="photo" role="img" aria-label="Young woman comforting an elderly woman on a sofa" style="background:linear-gradient(135deg,#b9b4ae,#8d8680 55%,#5a5653)"></div><h3>Emergency Care</h3><p>Mauris convallis id urna sit amet facilisis. Duis mollis vehicula neque id molestie</p><a class="more">Read More ▸</a></div>
  <a class="abs btn view-all">View All Services</a>
</section>

<section class="testimonials">
  <div class="abs testi-band"></div>
  <div class="abs testi-head"><div class="eyebrow">TESTMONIALS</div><h2>What our clients say about us</h2></div>
  <svg class="abs arrow" style="left:162px" width="18" height="36" viewBox="0 0 18 36"><path d="M16 2 2 18l14 16" fill="none" stroke="#9cc3dd" stroke-width="2"/></svg>
  <svg class="abs arrow" style="left:1020px" width="18" height="36" viewBox="0 0 18 36"><path d="M2 2l14 16L2 34" fill="none" stroke="#fff" stroke-width="2"/></svg>
  <div class="abs testi" style="left:188px;top:2317px"><svg width="58" height="36" viewBox="0 0 58 36" fill="#0b6ea8"><circle cx="13" cy="22" r="13"/><path d="M2 20C4 8 12 2 20 1L19 5C13 7 9 12 9 20z"/><circle cx="43" cy="22" r="13"/><path d="M32 20C34 8 42 2 50 1L49 5C43 7 39 12 39 20z"/></svg><p>Mauris convallis id urna sit amet facilisis. Duis mollis vehicula neque id molestie</p><div class="rule"></div><div class="avatar" role="img" aria-label="Client portrait"></div><h4>Vivamus magna</h4></div>
  <div class="abs testi" style="left:468px;top:2317px"><svg width="58" height="36" viewBox="0 0 58 36" fill="#0b6ea8"><circle cx="13" cy="22" r="13"/><path d="M2 20C4 8 12 2 20 1L19 5C13 7 9 12 9 20z"/><circle cx="43" cy="22" r="13"/><path d="M32 20C34 8 42 2 50 1L49 5C43 7 39 12 39 20z"/></svg><p>Mauris convallis id urna sit amet facilisis. Duis mollis vehicula neque id molestie</p><div class="rule"></div><div class="avatar" role="img" aria-label="Client portrait" style="background:linear-gradient(#e6d6bf,#c4a57e)"></div><h4>Vivamus magna</h4></div>
  <div class="abs testi" style="left:746px;top:2317px"><svg width="58" height="36" viewBox="0 0 58 36" fill="#0b6ea8"><circle cx="13" cy="22" r="13"/><path d="M2 20C4 8 12 2 20 1L19 5C13 7 9 12 9 20z"/><circle cx="43" cy="22" r="13"/><path d="M32 20C34 8 42 2 50 1L49 5C43 7 39 12 39 20z"/></svg><p>Mauris convallis id urna sit amet facilisis. Duis mollis vehicula neque id molestie</p><div class="rule"></div><div class="avatar" role="img" aria-label="Client portrait" style="background:linear-gradient(#cfdbe6,#5f8fb8)"></div><h4>Vivamus magna</h4></div>
</section>

<section class="contact">
  <div class="abs contact-bg" role="img" aria-label="Soft faded photo of caring hands"></div>
  <h2 class="abs contact-title">Let's get in touch!</h2>
  <p class="abs contact-text">Lorem ipsum dolor sit amet, consectetur adipiscing elit. Aenean egestas, ex non cursus sagittis, augue mi dictum massa, non tristique quam arcu vitae purus. Aan elementum sem eu lobortis euismod.</p>
  <div class="abs field" style="top:2727px;height:44px">Name</div>
  <div class="abs field" style="top:2780px;height:44px">Email</div>
  <div class="abs field" style="top:2833px;height:102px">Your Message</div>
  <a class="abs btn submit">Submit</a>
</section>

<section class="find-us">
  <div class="abs map" role="img" aria-label="Street map of the surrounding suburb"></div>
  <div class="abs find">
    <div class="eyebrow">CONTACT</div>
    <h2>How to Find Us</h2>
    <div class="row"><svg width="14" height="12" viewBox="0 0 24 20" fill="#fff"><path d="M0 8h24v12H0zM4 2h16v4H4z"/></svg><span>12 Elm Row, Westbury,<br>Australia</span></div>
    <div class="row"><svg width="13" height="13" viewBox="0 0 24 24" fill="#fff"><path d="M6.6 10.8a15 15 0 0 0 6.6 6.6l2.2-2.2a1 1 0 0 1 1-.25 11.4 11.4 0 0 0 3.6.6 1 1 0 0 1 1 1V20a1 1 0 0 1-1 1A17 17 0 0 1 3 4a1 1 0 0 1 1-1h3.5a1 1 0 0 1 1 1c0 1.25.2 2.45.6 3.6a1 1 0 0 1-.25 1z"/></svg><span>01 234 567 890</span></div>
    <div class="row"><svg width="13" height="10" viewBox="0 0 24 18" fill="#fff"><path d="M0 0h24v2L12 10 0 2z M0 4l12 8 12-8v14H0z"/></svg><span>hello@marlowhomecare.com</span></div>
    <div class="socials"><span></span><span></span><span></span><span></span></div>
  </div>
</section>

<footer>
  <div class="abs brand footer-brand"><span class="dot"></span><div>MARLOW<small>HOMECARE</small></div></div>
  <div class="abs copy">© 2022 <b>Marlow Home Care</b>. All right reserved</div>
  <div class="abs fcol" style="left:431px;top:3412px;width:240px"><h4>About Us</h4><p>Proin eu libro sit amt quam tinidunt fringilla. In accn imperdiet posuere. Nulla facilisi. Nullollicitudin lorem vitae porta consequat. Phasellus malesd luctus vulputate. Morbi eu leo fetum, susit ligula et, commodo arcu.</p></div>
  <div class="abs fcol" style="left:712px;top:3412px"><h4>Useful Links</h4><ul><li>Home</li><li>About</li><li>Services</li><li>FAQ</li><li>Contact</li></ul></div>
  <div class="abs fcol" style="left:862px;top:3412px"><h4>Serices</h4><ul><li>Medication Reminders</li><li>Domiciliary Care</li><li>Emergency Care</li><li>More</li></ul></div>
</footer>

</body>
</html>
```